Restaurant menu design

I need a menu for a restaurant in Spain.
It has to be bohemian but modern. We need something romantic and elegant.
The restaurant is elegant with good food and an excellent reputation. It is also modern at the same time.
The restaurant is superbly decorated and very chick so we need something "class" to fit in with the surroundings.
The size of the document must be 325 mm in high and 245 mm as a maximum and preferably made in indesign.

Reason: Thank you all for your designs.
So far all your designs are ok but it isn´t what we are looking for. Most of the designs are too loaded, too many colors and too much decoration.

Target Market(s)

Adults of various age groups and different nationalities mostly European.

Industry/Entity Type

Restaurant

Requirements
Must have
• The menu must have two interior pages with the text as in the document attached.It must be easily legible.
Nice to have
• See what kind of menus they use in important restaurants in places like Paris, see what designs are in trend, but Not necessarily doing the same style if it doesn’t fit in with the description above.
Should not have
• Nothing old fashioned.

```html
<!DOCTYPE html>
<html lang="es">
<head>
<meta charset="utf-8">
<title>Le Velours — Carta</title>
<link href="https://fonts.googleapis.com/css2?family=Italianno&family=EB+Garamond:ital,wght@1,400;1,500&display=swap" rel="stylesheet">
<style>
  :root{
    --canvas:#000;
    --panel:#111111;
    --band-top:#3a3a3a;
    --band-bottom:#1c1c1c;
    --title:#8e3a34;
    --item:#ececec;
    --desc:#7c7c7c;
    --price:#a07070;
    --rule:#1f1f1f;
    --gold-dark:#3a2608;
    --gold-mid:#8a6120;
    --gold-light:#c99a45;
    --rose:#a3121a;
    --rose-dark:#4a0508;
    --guitar:#9a4e1c;
  }
  *{margin:0;padding:0;box-sizing:border-box}
  html,body{width:1200px;height:796px;overflow:hidden;background:var(--canvas)}
  .menu{position:relative;width:1200px;height:796px;background:var(--canvas);
    font-family:"EB Garamond",Georgia,serif;font-style:italic}
  .page{position:absolute;top:50px;width:438px;height:695px;background:var(--panel)}
  .page--left{left:103px}
  .page--right{left:645px}
  .section{position:absolute;width:356px}
  .section__band{height:39px;background:linear-gradient(var(--band-top),var(--band-bottom));
    padding-left:5px;margin-bottom:8px}
  .section__title{font-family:"Italianno",cursive;font-weight:400;font-style:normal;
    font-size:36px;line-height:44px;color:var(--title);letter-spacing:.3px}
  .dishes{list-style:none;margin:0 7px 0 8px}
  .dish{display:flex;justify-content:space-between;align-items:flex-end;height:20.4px;
    padding-bottom:3px;border-bottom:1px solid var(--rule);font-size:11.5px;color:var(--item)}
  .dish--tall{height:40.8px}
  .dish__desc{color:var(--desc);font-size:9.5px}
  .dish__price{color:var(--price);white-space:nowrap;padding-left:8px}
  .sauces{position:absolute;left:680px;top:433px;font-size:10px;color:var(--item)}
  .sauces__label{font-family:"Italianno",cursive;font-style:normal;font-size:20px;color:var(--title)}
  .sauces__price{color:var(--price);font-size:7px;margin:0 4px}
  .art{position:absolute}
</style>
</head>
<body>
<main class="menu">
  <div class="art" role="img" aria-label="Carved gilded baroque frame with a cherub" style="left:0;top:0;width:100px;height:796px;background:linear-gradient(90deg,var(--gold-dark),var(--gold-light) 45%,var(--gold-mid) 75%,var(--gold-dark))"></div>
  <div class="art" role="img" aria-label="Red rose" style="left:0;top:615px;width:135px;height:181px;border-radius:0 60% 30% 0;background:radial-gradient(circle at 45% 45%,var(--rose),var(--rose-dark))"></div>
  <div class="art" role="img" aria-label="Carved gilded baroque frame" style="left:1135px;top:0;width:65px;height:796px;background:linear-gradient(90deg,var(--gold-dark),var(--gold-light) 50%,var(--gold-mid))"></div>
  <div class="art" role="img" aria-label="Acoustic guitar" style="left:1065px;top:470px;width:120px;height:326px;border-radius:40% 40% 20% 20%;background:linear-gradient(180deg,#2a1a10,var(--guitar) 55%,#5a2a0e)"></div>

  <section class="page page--left">
    <div class="section" style="left:42px;top:13px">
      <div class="section__band"><h2 class="section__title">Entradas / Ensaladas</h2></div>
      <ul class="dishes">
        <li class="dish"><span>Le Velours. <span class="dish__desc">Lechuga, tomate.</span></span><span class="dish__price">7,75 €</span></li>
        <li class="dish"><span>Ensalada Caprese <span class="dish__desc">(Tomate y Mozzarella)</span>.</span><span class="dish__price">7,75 €</span></li>
        <li class="dish"><span>Escarola al Queso de Cabra con Bacon.</span><span class="dish__price">6,75 €</span></li>
        <li class="dish"><span>Cocktail de Gambas, Langostinos y Aguacate.</span><span class="dish__price">7,50 €</span></li>
        <li class="dish"><span>La Sopa de Pescado.</span><span class="dish__price">8,25 €</span></li>
        <li class="dish"><span>Crema de Espárragos Trigueros y Calabacín.</span><span class="dish__price">5,95 €</span></li>
        <li class="dish"><span>Carpaccio de Ternera.</span><span class="dish__price">11,50 €</span></li>
        <li class="dish"><span>Carpaccio de Salmón al Eneldo.</span><span class="dish__price">9,75 €</span></li>
        <li class="dish"><span>Carpaccio de Atún.</span><span class="dish__price">13,95 €</span></li>
        <li class="dish"><span>Melón con Jamón Ibérico.</span><span class="dish__price">9,25 €</span></li>
        <li class="dish"><span>Parrillada de Verduras.</span><span class="dish__price">7,95 €</span></li>
        <li class="dish"><span>Parrillada de Verduras Gratinada al Queso de Cabra.</span><span class="dish__price">8,95 €</span></li>
        <li class="dish"><span>Gambas Roja de la Bahía.</span><span class="dish__price">12,95 €</span></li>
      </ul>
    </div>
    <div class="section" style="left:42px;top:348px">
      <div class="section__band"><h2 class="section__title">Pescados al Grill</h2></div>
      <ul class="dishes">
        <li class="dish"><span>Lubina al Hinojo.</span><span class="dish__price">15,50 €</span></li>
        <li class="dish"><span>Lubina Fileteada <span class="dish__desc">y su Salsa Rústica con Berenjena.</span></span><span class="dish__price">18,50 €</span></li>
        <li class="dish"><span>Filete de Rodaballo <span class="dish__desc">y su Salsa de Marisco.</span></span><span class="dish__price">17,25 €</span></li>
        <li class="dish"><span>Dorada del Mediterráneo.</span><span class="dish__price">13,95 €</span></li>
        <li class="dish"><span>Lenguado al Grill <span class="dish__desc">con Hierbas Provenzales.</span></span><span class="dish__price">20,75 €</span></li>
        <li class="dish"><span>Pieza de Atún Fresco <span class="dish__desc">y su Salsa Griviega.</span></span><span class="dish__price">18,95 €</span></li>
        <li class="dish"><span>Lomo de Salmón <span class="dish__desc">con Salsa de Frambuesa.</span></span><span class="dish__price">12,25 €</span></li>
        <li class="dish"><span>Parrillada <span class="dish__desc">de Pescado y Marisco</span>.</span><span class="dish__price">23,50 €</span></li>
      </ul>
    </div>
    <div class="section" style="left:42px;top:576px">
      <div class="section__band"><h2 class="section__title">Especial Niños</h2></div>
      <ul class="dishes">
        <li class="dish"><span>Solomillo Junior, huevo y patatas fritas.</span><span class="dish__price">6,25 €</span></li>
        <li class="dish"><span>Fish &amp; chips.</span><span class="dish__price">6,25 €</span></li>
      </ul>
    </div>
  </section>

  <section class="page page--right">
    <div class="section" style="left:42px;top:13px">
      <div class="section__band"><h2 class="section__title">Carnes</h2></div>
      <ul class="dishes">
        <li class="dish"><span>Pechuga de Pollo “Marie France” <span class="dish__desc">con Champiñones y Bacon.</span></span><span class="dish__price">11,95 €</span></li>
        <li class="dish"><span>Chuletas de Cordero.</span><span class="dish__price">24,50 €</span></li>
        <li class="dish"><span>Costillas de Cerdo con Salsa Barbacoa.</span><span class="dish__price">9,95 €</span></li>
        <li class="dish"><span>Paletilla de Cordero Lechal.</span><span class="dish__price">19,75 €</span></li>
        <li class="dish"><span>Le Strogonoff. <span class="dish__desc">Finas tiras de Solomillo con su Salsa de Champiñones.</span></span><span class="dish__price">15,90 €</span></li>
        <li class="dish"><span>Solomillo de Ternera.</span><span class="dish__price">18,50 €</span></li>
        <li class="dish dish--tall"><span>Solomillo de Ternera a la Ibérica <span class="dish__desc">con Jamón Ibérico y Ligera Salsa<br>de Vino Tinto.</span></span><span class="dish__price">20,75 €</span></li>
        <li class="dish dish--tall"><span>“Burger Salon Steak Haché”. <span class="dish__desc">Picada de Solomillo de Ternera,<br>Huevo Frito y Patatas Fritas</span></span><span class="dish__price">14,50 €</span></li>
        <li class="dish"><span>Solomillo de Cerdo al Horno <span class="dish__desc">con Bacon y su Salsa de Setas.</span></span><span class="dish__price">14,25 €</span></li>
        <li class="dish"><span>Entrecôte de Ternera.</span><span class="dish__price">14,75 €</span></li>
        <li class="dish"><span>T-Bone Steak de Ternera.</span><span class="dish__price">26,75 €</span></li>
        <li class="dish"><span>Chuletón de Ternera.</span><span class="dish__price">20,25 €</span></li>
        <li class="dish"><span>Parrillada <span class="dish__desc">de Carnes y Embutidos.</span></span><span class="dish__price">22,50 €</span></li>
      </ul>
    </div>
    <div class="section" style="left:42px;top:423px">
      <div class="section__band"><h2 class="section__title">Los Postres de Le Velours</h2></div>
      <ul class="dishes">
        <li class="dish"><span>Frambuesas “Le Velours”.</span><span class="dish__price">6,25 €</span></li>
        <li class="dish"><span>Cocktail de Frutas Exóticas.</span><span class="dish__price">5,25 €</span></li>
        <li class="dish"><span>Sorbete de Limón, Coulis de Fresa y Vodka.</span><span class="dish__price">5,50 €</span></li>
        <li class="dish"><span>Pastel de Chocolate Casero <span class="dish__desc">con su Salsa de Vainilla.</span></span><span class="dish__price">6,25 €</span></li>
        <li class="dish"><span>Crème Brulée.</span><span class="dish__price">6,25 €</span></li>
        <li class="dish"><span>Tarta de Manzana Casera “Tatín” <span class="dish__desc">y su Helado de Vainilla.</span></span><span class="dish__price">6,95 €</span></li>
        <li class="dish"><span>Copa Nievelia.</span><span class="dish__price">6,75 €</span></li>
        <li class="dish"><span>Pera al Chocolate Caliente <span class="dish__desc">y Helado de Macadamia.</span></span><span class="dish__price">5,95 €</span></li>
        <li class="dish"><span>Tarta de Queso <span class="dish__desc">con Coulis de Fresa.</span></span><span class="dish__price">5,75 €</span></li>
        <li class="dish"><span>Nuestra Mousse de Chocolate.</span><span class="dish__price">5,75 €</span></li>
      </ul>
    </div>
  </section>

  <p class="sauces"><span class="sauces__label">Salsas:</span> Pimienta. <span class="sauces__price">2,50 €</span> · Roquefort. <span class="sauces__price">2,50 €</span> · Bearnaise. <span class="sauces__price">2,50 €</span> · de Champiñones. <span class="sauces__price">2,50 €</span></p>
</main>
</body>
</html>
```